Communication and Marketing agency needs a new presentation card

We are a group of communication and marketing agencies specialized in companies that are in the logistics and industrial sector. The head agency is TELVANO Grupo and the group consists of 4 agencies: TELVANO Media, TELVANO Digital, TELVANO Research and EnlazaPorImagen. We hace 4 offices in Spain (Madrid, Barcelona, Valencia and Murcia). We are looking for a clean and attractive design that transmits our experience, brand presence in the market and knowledge to those who receive the card.It has to maintain the colors of the logo that is attached.
Target Market(s)
logistics and industrial sector
Marketing department
Clean and attractive design

```html
<!DOCTYPE html>
<html lang="es">
<head>
<meta charset="utf-8">
<title>TELVANO Grupo – Tarjetas de presentación</title>
<link href="https://fonts.googleapis.com/css2?family=Jost:wght@300;400;500&display=swap" rel="stylesheet">
<style>
  :root{
    --red:#b81f2c;
    --red-light:#c52a37;
    --red-dark:#a81a26;
    --white:#ffffff;
    --grey:#555555;
    --stage:#2b2b2b;
  }
  *{margin:0;padding:0;box-sizing:border-box}
  html,body{width:1200px;height:892px;overflow:hidden}
  body{
    background:var(--stage);
    font-family:"Jost",sans-serif;
    display:flex;align-items:center;justify-content:center;gap:40px;
  }
  .card{
    width:540px;height:310px;position:relative;overflow:hidden;
    box-shadow:0 12px 30px rgba(0,0,0,.45);
  }
  /* Front */
  .card--front{
    background:linear-gradient(160deg,var(--red-light),var(--red-dark));
  }
  .front__logo{
    position:absolute;top:70px;left:0;right:0;text-align:center;
    color:var(--white);font-weight:300;font-size:46px;letter-spacing:4px;line-height:1;
  }
  .front__logo .sub{display:block;font-size:24px;letter-spacing:1px;margin-top:6px;padding-left:160px}
  .front__band{
    position:absolute;left:0;right:0;top:196px;height:72px;background:var(--white);
    display:flex;align-items:center;justify-content:space-around;padding:0 14px;
  }
  .agency{font-weight:400;font-size:15px;letter-spacing:1px;line-height:1.05;text-align:center}
  .agency small{display:block;font-size:11px;letter-spacing:.5px}
  .agency--grey{color:var(--grey)}
  .agency--red{color:var(--red)}
  /* Back */
  .card--back{background:var(--white)}
  .back__brand{position:absolute;left:34px;top:178px}
  .back__logo{color:var(--red);font-weight:300;font-size:36px;letter-spacing:3px;line-height:1}
  .back__logo .sub{font-size:20px;color:var(--grey);letter-spacing:1px;margin-left:6px}
  .back__cities{margin-top:14px;color:var(--grey);font-size:12px;display:flex;align-items:center;gap:6px}
  .back__cities .dot{width:5px;height:5px;border-radius:50%;background:var(--red)}
  .back__panel{
    position:absolute;right:0;top:36px;width:250px;height:232px;background:var(--red);
    color:var(--white);padding:22px 18px 0 10px;text-align:right;
  }
  .contact__name{font-size:22px;font-weight:400;line-height:1.1}
  .contact__role{font-size:12px;font-weight:300;margin-bottom:16px}
  .contact__list{list-style:none;font-size:13px;font-weight:300;line-height:1.65}
  .contact__list li{display:flex;align-items:center;justify-content:flex-end;gap:8px}
  .icon{width:12px;height:12px;flex:none}
</style>
</head>
<body>

<section class="card card--front" aria-label="Anverso de la tarjeta">
  <div class="front__logo">TELVANO<span class="sub">Grupo</span></div>
  <div class="front__band">
    <div class="agency agency--grey">TELVANO<small>Digital</small></div>
    <div class="agency agency--red">TELVANO<small>Media</small></div>
    <div class="agency agency--grey">TELVANO<small>Research</small></div>
    <div class="agency agency--red">EnlazaPorImagen</div>
  </div>
</section>

<section class="card card--back" aria-label="Reverso de la tarjeta">
  <div class="back__brand">
    <div class="back__logo">TELVANO<span class="sub">Media</span></div>
    <div class="back__cities">
      <span>Madrid</span><span class="dot"></span>
      <span>Barcelona</span><span class="dot"></span>
      <span>Valencia</span><span class="dot"></span>
      <span>Murcia</span>
    </div>
  </div>
  <div class="back__panel">
    <div class="contact__name">Lorenzo Vidal</div>
    <div class="contact__role">Director</div>
    <ul class="contact__list">
      <li>912 470 385
        <svg class="icon" viewBox="0 0 12 12" aria-hidden="true"><path d="M3 1l2 2-1 1.5c.7 1.4 1.6 2.3 3 3L8.5 6.5l2 2-1.5 1.8C5.5 10 2 6.5 1.7 3z" fill="#fff"/></svg></li>
      <li>655 218 047
        <svg class="icon" viewBox="0 0 12 12" aria-hidden="true"><rect x="3" y="0.5" width="6" height="11" rx="1" fill="none" stroke="#fff"/><circle cx="6" cy="9.5" r=".7" fill="#fff"/></svg></li>
      <li>lvidal@telvano.es
        <svg class="icon" viewBox="0 0 12 12" aria-hidden="true"><rect x=".5" y="2.5" width="11" height="7" fill="none" stroke="#fff"/><path d="M.5 2.5L6 7l5.5-4.5" fill="none" stroke="#fff"/></svg></li>
      <li>lorenzovidal
        <svg class="icon" viewBox="0 0 12 12" aria-hidden="true"><rect x="1" y="1" width="10" height="10" fill="#fff"/></svg></li>
      <li>www.telvano.es
        <svg class="icon" viewBox="0 0 12 12" aria-hidden="true"><circle cx="6" cy="6" r="5" fill="#fff"/></svg></li>
    </ul>
  </div>
</section>

</body>
</html>
```